Flyer for IT Support Company

We need a 1 sided A5 flyer to promote our services and support packages to local businesses, I have attached the sort of content and layout we are looking for but happy for you to be creative with backgrounds and colors. It needs to look modern and professional but catch the eye ;-)
The strap-line on the logo needs to be changed to to 'Your Local IT Company'

It Company

```html
<!DOCTYPE html>
<html lang="en">
<head>
<meta charset="utf-8">
<title>Brightnet – Affordable IT Support Packages</title>
<link rel="stylesheet" href="https://fonts.googleapis.com/css2?family=Arimo:wght@400;700&family=Oswald:wght@600;700&family=Archivo+Black&display=swap">
<style>
  :root {
    --green-deep: #0f4a14;
    --pink: #e8198b;
    --pink-dark: #b0105f;
    --teal: #4fe0b0;
    --panel: rgba(90, 110, 90, 0.55);
    --row: rgba(40, 120, 40, 0.55);
    --row-head: rgba(10, 60, 15, 0.8);
    --white: #ffffff;
    --ink: #1c1c1c;
    --grey-light: #f2f2f2;
    --pill-green: #8aa52b;
  }
  * { box-sizing: border-box; margin: 0; padding: 0; }
  html, body { width: 856px; height: 1200px; overflow: hidden; }
  body { font-family: "Arimo", Arial, sans-serif; background: var(--white); }

  .flyer { position: relative; width: 856px; height: 1200px; overflow: hidden;
    background: linear-gradient(180deg, var(--grey-light) 0%, var(--white) 100%); }

  .hero-backdrop { position: absolute; left: 0; top: 0; width: 856px; height: 900px;
    background:
      radial-gradient(ellipse at 30% 25%, rgba(190,255,90,0.55), transparent 55%),
      radial-gradient(ellipse at 85% 55%, rgba(160,240,60,0.45), transparent 50%),
      linear-gradient(160deg, #3fa82a 0%, #1e6e1a 45%, #5cc42a 75%, #a8e840 100%); }

  .hero-person { position: absolute; left: 380px; top: 0; width: 330px; height: 260px;
    background: radial-gradient(ellipse at 50% 40%, rgba(120,80,60,0.55), rgba(60,90,50,0.0) 70%); }

  .bottom-wave { position: absolute; left: 0; top: 800px; width: 856px; height: 400px; }

  .brand { position: absolute; left: 560px; top: 60px; height: 44px;
    display: flex; align-items: center; gap: 12px; }
  .brand-dot { width: 30px; height: 30px; border-radius: 50%; background: var(--white); }
  .brand-name { font-family: "Arimo", Arial, sans-serif; font-weight: 700; font-size: 38px;
    color: var(--white); line-height: 1; }

  .title-banner { position: absolute; left: 107px; top: 258px; width: 640px; height: 97px;
    background: linear-gradient(180deg, #f0459e 0%, var(--pink) 50%, var(--pink-dark) 100%);
    border: 2px solid rgba(255,255,255,0.85); text-align: center; }
  .title-main { font-family: "Oswald", Impact, sans-serif; font-weight: 700; font-size: 37px;
    letter-spacing: 2.5px; color: var(--white); line-height: 58px;
    text-shadow: 0 2px 2px rgba(0,0,0,0.45); }
  .title-sub { font-family: "Arimo", Arial, sans-serif; font-weight: 700; font-size: 20px;
    letter-spacing: 1px; color: var(--white); line-height: 20px; margin-top: 8px; }
  .title-divider { position: absolute; left: 0; top: 56px; width: 100%; height: 2px;
    background: rgba(255,255,255,0.85); }

  .package-panel { position: absolute; left: 130px; top: 360px; width: 590px; height: 570px;
    background: var(--panel); border: 2px solid rgba(255,255,255,0.45); border-radius: 8px;
    box-shadow: 0 4px 10px rgba(0,0,0,0.35); }

  .package-table { position: absolute; left: 150px; top: 375px; width: 551px;
    border-collapse: collapse; color: var(--white); font-size: 15px; }
  .package-table td { height: 21.75px; padding: 0 5px; border: 1px solid rgba(255,255,255,0.35);
    background: var(--row); white-space: nowrap; }
  .package-table .col-label { width: 246px; }
  .package-table .col-remote { width: 71px; }
  .package-table .col-plus { width: 73px; }
  .package-table .col-pro { width: 73px; }
  .package-table tr.price-row td { background: var(--row-head); }
  .package-table tr.section-row td { background: var(--pink); text-align: center;
    font-weight: 700; border-color: var(--pink); }

  .promo-badge { position: absolute; left: 645px; top: 780px; width: 160px; height: 155px; }
  .promo-text { position: absolute; left: 660px; top: 800px; width: 140px; text-align: center;
    transform: rotate(-28deg); transform-origin: center; color: var(--ink);
    font-size: 12px; line-height: 14px; }
  .promo-price { font-family: "Archivo Black", "Arial Black", sans-serif; font-size: 22px; line-height: 25px; }
  .promo-place { font-family: "Archivo Black", "Arial Black", sans-serif; font-size: 13px; }

  .feature-row { position: absolute; left: 30px; top: 970px; width: 800px; display: flex;
    justify-content: space-between; }
  .feature { width: 170px; text-align: center; color: var(--ink); font-size: 16px; line-height: 21px; }
  .feature svg { display: block; margin: 0 auto 6px; height: 50px; }

  .divider-line { position: absolute; left: 45px; top: 1072px; width: 766px; height: 1px; background: #cfcfcf; }

  .call-to-action { position: absolute; left: 0; top: 1076px; width: 856px; text-align: center;
    color: var(--pink); font-weight: 700; font-size: 21px; line-height: 26px; }

  .contact-pill { position: absolute; top: 1138px; height: 27px; border-radius: 14px;
    font-size: 18px; line-height: 27px; text-align: center; color: var(--ink);
    box-shadow: 0 0 6px rgba(0,0,0,0.25); white-space: nowrap; }
  .contact-phone { left: 52px; width: 184px; background: var(--pill-green); }
  .contact-email { left: 306px; width: 226px; background: var(--pink); }
  .contact-web { left: 585px; width: 220px; background: var(--pill-green); }
</style>
</head>
<body>
<main class="flyer">
  <div class="hero-backdrop" role="img" aria-label="Green digital network background with floating hexagon technology icons"></div>
  <div class="hero-person" role="img" aria-label="Photograph of a businessman in glasses touching a virtual screen"></div>

  <svg class="bottom-wave" viewBox="0 0 856 400" aria-hidden="true">
    <polygon points="0,20 428,80 856,20 856,60 428,110 0,60" fill="#0f4a14"/>
    <polygon points="0,55 428,105 856,55 856,400 0,400" fill="#f4f4f4"/>
  </svg>

  <div class="brand">
    <span class="brand-dot"></span>
    <span class="brand-name">Brightnet</span>
  </div>

  <header class="title-banner">
    <h1 class="title-main">AFFORDABLE IT SUPPORT PACKAGES</h1>
    <div class="title-divider"></div>
    <p class="title-sub">Peace of Mind for your Business at Competitive Prices</p>
  </header>

  <div class="package-panel"></div>
  <table class="package-table">
    <colgroup><col class="col-label"><col class="col-remote"><col class="col-plus"><col class="col-pro"><col></colgroup>
    <tr class="price-row"><td>IT Support Packages</td><td>Remote</td><td>Plus</td><td>Pro</td><td>Unlimited</td></tr>
    <tr class="price-row"><td>Per Server</td><td>£45pm</td><td>£85pm</td><td>£85pm</td><td>£85pm</td></tr>
    <tr class="price-row"><td>Per Computers</td><td>£10pm</td><td>£10pm</td><td>£13pm</td><td>£15pm</td></tr>
    <tr class="section-row"><td colspan="5">Support Service</td></tr>
    <tr><td>Server support</td><td>✓</td><td>✓</td><td>✓</td><td>✓</td></tr>
    <tr><td>PC/device support</td><td>✓</td><td>✓</td><td>✓</td><td>✓</td></tr>
    <tr class="section-row"><td colspan="5">Server/Network Callout</td></tr>
    <tr><td>Remote support</td><td>✓</td><td>✓</td><td>✓</td><td>✓</td></tr>
    <tr><td>Onsite callout (4hr response)</td><td>£40</td><td>✓</td><td>✓</td><td>✓</td></tr>
    <tr><td>Hourly rate onsite</td><td>£25ph</td><td>Included</td><td>Included</td><td>Included</td></tr>
    <tr class="section-row"><td colspan="5">Computer/Equipment/Device Callout</td></tr>
    <tr><td>Remote support</td><td></td><td></td><td></td><td>✓</td></tr>
    <tr><td>Onsite callout (4hr response)</td><td>£40</td><td>£40</td><td></td><td>✓</td></tr>
    <tr><td>Hourly rate onsite</td><td>£25ph</td><td>£25ph</td><td>Included</td><td>Included</td></tr>
    <tr class="section-row"><td colspan="5">Protection/Security</td></tr>
    <tr><td>Sentra anti-virus (per PC)</td><td>£2</td><td>£2</td><td>£2</td><td>✓</td></tr>
    <tr><td>Sentra content filter (per PC)</td><td>£1.30</td><td>£1.30</td><td>£1.30</td><td>✓</td></tr>
    <tr><td>Remote back-up (per unit, 5GB)</td><td>£1.50</td><td>£1.50</td><td>£1.50</td><td>✓</td></tr>
    <tr class="section-row"><td colspan="5">Monitoring</td></tr>
    <tr><td>Daily back-up checks</td><td>✓</td><td>✓</td><td>✓</td><td>✓</td></tr>
    <tr><td>24/7 monitoring</td><td>✓</td><td>✓</td><td>✓</td><td>✓</td></tr>
    <tr class="section-row"><td colspan="5">Maintenance</td></tr>
    <tr><td>Patch management</td><td>✓</td><td>✓</td><td>✓</td><td>✓</td></tr>
    <tr><td>Software updates</td><td>✓</td><td>✓</td><td>✓</td><td>✓</td></tr>
    <tr><td>Security updates</td><td>✓</td><td>✓</td><td>✓</td><td>✓</td></tr>
  </table>

  <svg class="promo-badge" viewBox="0 0 160 155" aria-hidden="true">
    <polygon points="50,4 132,18 158,90 112,150 30,138 3,66" fill="#4fe0b0" stroke="#ffffff" stroke-width="2"/>
  </svg>
  <div class="promo-text">
    IT Support from<br><span class="promo-price">£10pm</span> -<br>from a<br>trusted provider<br>based in<br><span class="promo-place">Marlowby</span>
  </div>

  <section class="feature-row">
    <div class="feature">
      <svg viewBox="0 0 60 50" aria-hidden="true">
        <circle cx="24" cy="28" r="14" fill="#e8198b"/><circle cx="24" cy="28" r="5" fill="#f4f4f4"/>
        <circle cx="44" cy="14" r="8" fill="#8fcf2a"/><circle cx="44" cy="14" r="3" fill="#f4f4f4"/>
      </svg>
      Affordable, Local<br>Service
    </div>
    <div class="feature">
      <svg viewBox="0 0 60 50" aria-hidden="true">
        <path d="M14 30 V22 a16 16 0 0 1 32 0 V30" fill="none" stroke="#888" stroke-width="3"/>
        <rect x="9" y="24" width="9" height="14" rx="3" fill="#e8198b"/>
        <rect x="42" y="24" width="9" height="14" rx="3" fill="#e8198b"/>
      </svg>
      4 Hour<br>Callout
    </div>
    <div class="feature">
      <svg viewBox="0 0 60 50" aria-hidden="true">
        <rect x="4" y="12" width="24" height="18" fill="#8fcf2a" stroke="#777" stroke-width="2"/>
        <rect x="32" y="12" width="24" height="18" fill="#e8198b" stroke="#777" stroke-width="2"/>
        <rect x="2" y="34" width="56" height="6" fill="#aaa"/>
        <line x1="4" y1="4" x2="56" y2="4" stroke="#777" stroke-width="3"/>
      </svg>
      Remote<br>Support
    </div>
    <div class="feature">
      <svg viewBox="0 0 60 50" aria-hidden="true">
        <rect x="8" y="4" width="40" height="30" fill="#8fcf2a" stroke="#666" stroke-width="2"/>
        <rect x="22" y="34" width="12" height="8" fill="#888"/>
        <circle cx="30" cy="18" r="7" fill="none" stroke="#333" stroke-width="2.5"/>
        <line x1="35" y1="23" x2="44" y2="32" stroke="#333" stroke-width="3"/>
      </svg>
      24/7<br>Monitoring
    </div>
    <div class="feature">
      <svg viewBox="0 0 60 50" aria-hidden="true">
        <ellipse cx="28" cy="28" rx="20" ry="15" fill="#e8198b"/>
        <rect x="18" y="38" width="5" height="8" fill="#e8198b"/><rect x="32" y="38" width="5" height="8" fill="#e8198b"/>
        <rect x="48" y="30" width="5" height="16" fill="#ccc"/><rect x="54" y="36" width="5" height="10" fill="#ccc"/>
      </svg>
      Server/PC Builds<br>from £250
    </div>
  </section>

  <div class="divider-line"></div>

  <p class="call-to-action">Protect your business and keep downtime costs at bay<br>Call, email or live chat with us on our website today!</p>

  <div class="contact-pill contact-phone">01632 960 451</div>
  <div class="contact-pill contact-email">info@brightnet.example</div>
  <div class="contact-pill contact-web">www.brightnet.example</div>
</main>
</body>
</html>
```